New Dental Office Needs an Attractive and user friendly Website Designed

I need a website for a new dental office. The Name is Larkhaven Dentistry. I would like a Modern design with a user friendly interface and usability.
I would like a landing page, a page that lists the services we offer: Cosmetic Dentistry, Implants, Dental Hygiene, Emergency Services, Restorations, Dentures
Target Market(s)
Mid to upper class
Industry/Entity Type
Dentistry
Coding
Coded - Design and coding required
Number of Pages Required
1 page
Requirements
Must have
- Landing page that has a scheduling option, Procedures, operating hours, and contact us info
Nice to have
- Appealing design, Soft comforting colors. Easy to navigate page, Modern and professional.

```html
<!DOCTYPE html>
<html lang="en">
<head>
<meta charset="utf-8">
<title>Larkhaven Dentistry</title>
<link href="https://fonts.googleapis.com/css2?family=Cormorant+Garamond:wght@500;600&family=Lato:wght@400;700&display=swap" rel="stylesheet">
<style>
:root{
  --cream:#f9f6f1;
  --sand:#f1ece4;
  --box:#efe9e0;
  --green:#3f5a3e;
  --sage:#6e7d5e;
  --taupe:#a39a86;
  --ink:#3a3a36;
  --mint:#b9dccd;
  --white:#ffffff;
}
*{box-sizing:border-box;margin:0;padding:0}
html,body{width:1200px;height:5164px;overflow:hidden}
body{font-family:"Lato",sans-serif;color:var(--ink);background:var(--cream)}
.serif{font-family:"Cormorant Garamond",serif}
section,header,footer{position:relative;width:1200px}
.btn{display:inline-block;background:var(--taupe);color:var(--white);font-size:20px;text-decoration:none;padding:12px 24px;border-radius:3px}
h2.title{font-family:"Cormorant Garamond",serif;font-weight:600;color:var(--green);letter-spacing:2px}
.photo{position:absolute}

.topbar{height:40px;background:#f3efe8;display:flex;align-items:center;justify-content:space-between;padding:0 92px 0 92px;font-size:15px}
.topbar .phone{display:flex;align-items:center;gap:8px}
.topbar .social{display:flex;gap:10px}
.topbar .social span{width:18px;height:18px;background:var(--green);border-radius:3px;display:block}

.nav{height:96px;background:var(--cream);border-bottom:2px solid var(--mint);display:flex;align-items:center;padding:0 88px 0 96px}
.brand{font-family:"Cormorant Garamond",serif;font-weight:600;font-size:32px;color:var(--green)}
.nav ul{list-style:none;display:flex;gap:58px;margin-left:auto;margin-right:88px;font-size:18px}
.nav .btn{padding:12px 24px}

.hero{height:528px;background:var(--cream)}
.hero h1{position:absolute;left:88px;top:96px;font-family:"Cormorant Garamond",serif;font-weight:600;font-size:60px;line-height:68px;color:var(--green);letter-spacing:2px}
.hero p{position:absolute;left:88px;top:254px;font-size:28px;line-height:44px}
.hero .btn{position:absolute;left:88px;top:360px}
.hero .photo{left:660px;top:0;width:540px;height:528px;background:linear-gradient(135deg,#efe6da,#d9bfa3 55%,#b98a66)}

.about{height:270px;background:var(--sand)}
.about h2{position:absolute;left:88px;top:96px;font-size:54px}
.about p{position:absolute;left:346px;top:92px;width:780px;font-size:24px;line-height:31px}

.services{height:1014px;background:var(--cream);text-align:center}
.services h2{position:absolute;top:92px;width:100%;font-size:52px}
.services .sub{position:absolute;top:170px;width:100%;font-size:24px}
.svc{position:absolute;width:348px;text-align:center}
.svc svg{width:84px;height:84px;display:block;margin:0 auto}
.svc h3{margin-top:26px;font-size:24px;font-weight:700;color:var(--green)}
.svc p{margin-top:12px;font-size:15px;line-height:24px;color:#555}
.svc .btn{margin-top:28px;padding:12px 24px}

.prioritize{height:384px;background:var(--sage);color:var(--white)}
.prioritize h2{position:absolute;left:88px;top:78px;font-size:52px;color:var(--white)}
.prioritize p{position:absolute;left:88px;top:160px;font-size:24px;line-height:34px}
.prioritize .btn{position:absolute;left:88px;top:256px;background:var(--white);color:var(--green);border-radius:6px;padding:10px 22px}

.hours{height:950px;background:var(--cream)}
.hours h2{position:absolute;left:88px;top:94px;font-size:52px;line-height:70px}
.hours .table{position:absolute;left:88px;top:278px;width:468px;height:380px;background:var(--box);border-radius:8px;padding:42px 0 0 32px}
.hours table{border-collapse:collapse;font-size:24px}
.hours td{height:42.5px;padding:0}
.hours td:first-child{width:182px}
.hours address{position:absolute;left:106px;top:700px;font-style:normal;font-size:24px;line-height:32px}
.hours .btn{position:absolute;left:106px;top:788px}
.hours .photo{left:616px;top:92px;width:496px;height:742px;background:linear-gradient(160deg,#f1e9dd,#e4d7c4 60%,#d4c3a8)}

.reviews{height:582px;background:var(--sand)}
.reviews h2{position:absolute;top:104px;width:100%;text-align:center;font-size:52px}
.card{position:absolute;top:214px;width:320px;height:274px;background:var(--white);border-radius:6px;padding:34px 40px;font-size:19px;line-height:34px}
.card .q{font-family:"Cormorant Garamond",serif;font-size:64px;line-height:40px;color:#c8b48f;height:40px}
.card .who{margin-top:22px;font-weight:700}

.book{height:552px;background:var(--cream)}
.book h2{position:absolute;left:88px;top:120px;font-size:52px;line-height:68px}
.book p{position:absolute;left:88px;top:278px;font-size:24px;line-height:36px}
.book .btn{position:absolute;left:88px;top:382px}
.book .photo{left:632px;top:0;width:568px;height:552px;background:linear-gradient(135deg,#f3ead9,#e2c9a2 55%,#c8a57c)}

.newsletter{height:384px;background:var(--sand);text-align:center}
.newsletter h2{position:absolute;top:82px;width:100%;font-size:52px}
.newsletter p{position:absolute;top:166px;width:100%;font-size:24px;color:var(--green)}
.newsletter form{position:absolute;left:306px;top:240px;display:flex}
.newsletter .field{width:394px;height:60px;background:var(--white);border:1px solid #e2ddd4;font-size:20px;padding:0 36px;display:flex;align-items:center;color:var(--ink)}
.newsletter .btn{height:60px;width:196px;font-size:28px;padding:0;display:flex;align-items:center;justify-content:center;border-radius:4px}

.site-footer{height:364px;background:var(--white);text-align:center;font-size:17px}
.site-footer .brand{position:absolute;top:60px;width:100%;font-size:40px}
.site-footer nav{position:absolute;top:152px;width:100%;display:flex;justify-content:center;gap:48px}
.site-footer .legal{position:absolute;top:208px;width:100%}
.site-footer .copy{position:absolute;top:256px;width:100%}
</style>
</head>
<body>

<div class="topbar">
  <div class="phone">
    <svg width="12" height="18" viewBox="0 0 12 18"><rect x="1" y="1" width="10" height="16" rx="2" fill="var(--green)"/></svg>
    (555) 010-2849
  </div>
  <div class="social"><span></span><span></span><span></span></div>
</div>

<header class="nav">
  <div class="brand">Larkhaven Dentistry</div>
  <ul><li>Services</li><li>About</li><li>Contact</li></ul>
  <a class="btn" href="#book">Book Online</a>
</header>

<section class="hero">
  <h1>Advance Care with<br>a Gentle Touch</h1>
  <p>Advanced Care with a Gentle Touch.<br>Because Your Smile Deserves the Best.</p>
  <a class="btn" href="#book">Schedule Appointment</a>
  <div class="photo" role="img" aria-label="Photo of a smiling woman touching her cheek"></div>
</section>

<section class="about">
  <h2 class="title">About Us</h2>
  <p>Providing exceptional dental care in a tranquil, spa-like setting. We cater to your individual needs with state-of-the-art technology and a gentle personal approach.</p>
</section>

<section class="services">
  <h2 class="title">Our Services</h2>
  <p class="sub">Comprehensive Dental Solutions, Tailored to You.</p>

  <div class="svc" style="left:78px;top:282px">
    <svg viewBox="0 0 84 84" fill="none" stroke="var(--green)" stroke-width="2.5" stroke-linejoin="round"><path d="M22 14c-8 0-12 7-12 16 0 10 6 14 7 24 1 9 2 20 7 20s5-16 11-16 6 16 11 16 6-11 7-20c1-8 5-12 5-18"/><path d="M22 14c6 0 9 3 14 3s6-2 10-3"/><path d="M62 8l3 8 8 3-8 3-3 8-3-8-8-3 8-3z"/></svg>
    <h3>Cosmetic Dentistry</h3>
    <p>Whitening, veneers, and smile<br>makeovers for a confident appearance.</p>
    <a class="btn" href="#">Learn More</a>
  </div>
  <div class="svc" style="left:426px;top:282px">
    <svg viewBox="0 0 84 84" fill="none" stroke="var(--green)" stroke-width="2.5" stroke-linejoin="round"><path d="M28 10c-6 0-8 5-7 10 1 6 6 8 21 8s20-2 21-8c1-5-1-10-7-10-5 0-8 3-14 3s-9-3-14-3z"/><path d="M32 34h20M34 42h16M36 50h12M38 58h8"/><path d="M38 62l4 12 4-12"/></svg>
    <h3>Dental Implants</h3>
    <p>Permanent tooth replacement<br>with natural look, feel, and function.</p>
    <a class="btn" href="#">Learn More</a>
  </div>
  <div class="svc" style="left:774px;top:282px">
    <svg viewBox="0 0 84 84" fill="none" stroke="var(--green)" stroke-width="2.5" stroke-linejoin="round"><path d="M10 72l40-36 4 4-40 36z"/><path d="M18 60l4 4M24 55l4 4M30 50l4 4"/><path d="M66 10c4 6 8 10 8 14a8 8 0 0 1-16 0c0-4 4-8 8-14z"/></svg>
    <h3>Hygiene &amp; Cleanings</h3>
    <p>Thorough, professional cleanings<br>to protect your oral health.</p>
    <a class="btn" href="#">Learn More</a>
  </div>
  <div class="svc" style="left:78px;top:642px">
    <svg viewBox="0 0 84 84" fill="none" stroke="var(--green)" stroke-width="2.5" stroke-linejoin="round"><path d="M42 8l28 10v20c0 18-12 30-28 38C26 68 14 56 14 38V18z"/><path d="M36 28h12v8h8v12h-8v8H36v-8h-8V36h8z"/></svg>
    <h3>Emergency Services</h3>
    <p>Prompt, compassionate care<br>when dental issues can't wait.</p>
    <a class="btn" href="#">Learn More</a>
  </div>
  <div class="svc" style="left:426px;top:642px">
    <svg viewBox="0 0 84 84" fill="none" stroke="var(--green)" stroke-width="2.5" stroke-linejoin="round"><path d="M26 8c-9 0-14 8-13 18 1 10 6 14 7 24 1 10 3 26 9 26s5-22 13-22 7 22 13 22 8-16 9-26c1-10 6-14 7-24 1-10-4-18-13-18-6 0-10 4-16 4s-10-4-16-4z"/><path d="M30 20c4 0 8 3 12 3"/></svg>
    <h3>Restorations</h3>
    <p>Repair and strengthen teeth<br>with expertly crafted solutions.</p>
    <a class="btn" href="#">Learn More</a>
  </div>
  <div class="svc" style="left:774px;top:642px">
    <svg viewBox="0 0 84 84" fill="none" stroke="var(--green)" stroke-width="2.5" stroke-linejoin="round"><path d="M6 30c10 6 22 8 36 8s26-2 36-8c0 14-6 22-14 22H20C12 52 6 44 6 30z"/><path d="M22 40v12M32 42v12M42 42v12M52 42v12M62 40v12"/></svg>
    <h3>Dentures &amp; Partials</h3>
    <p>Custom full or partial dentures<br>designed for comfort and fit.</p>
    <a class="btn" href="#">Learn More</a>
  </div>
</section>

<section class="prioritize">
  <h2 class="title">Time to Prioritize Yourself.</h2>
  <p>Book your appointment with Larkhaven Dentistry and experience our calming<br>Environment and personalized attention first hand.</p>
  <a class="btn" href="#book">Learn More</a>
</section>

<section class="hours">
  <h2 class="title">Office Hours<br>&amp; Location</h2>
  <div class="table">
    <table>
      <tr><td>Monday</td><td>8:00 AM - 5:00 PM</td></tr>
      <tr><td>Tuesday</td><td>8:00 AM - 5:00 PM</td></tr>
      <tr><td>Wednesday</td><td>9:00 AM - 6:00 PM</td></tr>
      <tr><td>Thursday</td><td>8:00 AM - 5:00 PM</td></tr>
      <tr><td>Friday</td><td>8:00 AM - 2:00 PM</td></tr>
      <tr><td>Saturday</td><td>Closed</td></tr>
      <tr><td>Sunday</td><td>Closed</td></tr>
    </table>
  </div>
  <address>48 Alder Lane<br>Brookfield, IL 62704</address>
  <a class="btn" href="#">Get Directions</a>
  <div class="photo" role="img" aria-label="Photo of a cream armchair beside a potted fiddle-leaf fig in a calm waiting room"></div>
</section>

<section class="reviews">
  <h2 class="title">What Our Patients Are Saying</h2>
  <div class="card" style="left:88px;text-align:center">
    <div class="q" style="text-align:left">&ldquo;</div>
    <p>The staff is very friendly and professional. Highly recommend this office!</p>
    <p class="who" style="text-align:left">- Nora P</p>
  </div>
  <div class="card" style="left:440px">
    <div class="q">&ldquo;</div>
    <p>My experience with the Doctor was fantastic.<br>I feel confident in my smile.</p>
    <p class="who">- Derek L</p>
  </div>
  <div class="card" style="left:792px">
    <div class="q">&ldquo;</div>
    <p>I had an emergency and Got same-day treatment. So grateful for the care!</p>
    <p class="who">- Maya T</p>
  </div>
</section>

<section class="book" id="book">
  <h2 class="title">Book an<br>Appointment</h2>
  <p>Ready for a healthier smile?<br>Scheduling your visit is quick and easy.</p>
  <a class="btn" href="#">Schedule Now</a>
  <div class="photo" role="img" aria-label="Photo of a smiling blonde woman in a cream sweater"></div>
</section>

<section class="newsletter">
  <h2 class="title">Subscribe to Our Newsletter</h2>
  <p>Stay up to date with our latest news and dental tips.</p>
  <form>
    <div class="field">Enter your email address</div>
    <a class="btn" href="#">Subscribe</a>
  </form>
</section>

<footer class="site-footer">
  <div class="brand">Larkhaven Dentistry</div>
  <nav><span>Home</span><span>Services</span><span>About</span><span>Contact</span></nav>
  <p class="legal">Privacy Policy | Terms</p>
  <p class="copy">© 2025 Larkhaven Dentistry. All rights reserved.</p>
</footer>

</body>
</html>
```